Selka Marven Photography Business Card

I need a new business card/ possibly design to use for other marking materials ... I have included my logo below in a few different colors, but can also provide the logo in additional colors and sizes. I would love a card the expresses clean, simple and classy.

Target Market(s)

Portrait photography clients, child photography clients

Industry/Entity Type

Photographer

Contact Information for Business Card

Selka Marven Photography, Alder Falls VT, www.selkamarvenphotography-demo.com
T. 555-203-1946 E. selkamarvenphoto@mailbox-demo.com

Colors
33b8a4
eea4c8
5c5c5c

Requirements
Must have
• I would like to include my logo on card.
Nice to have
• I also like the color brown as well as the choices below. I would like a simple, elegant card, something classy.

```html
<!DOCTYPE html>
<html lang="en">
<head>
<meta charset="utf-8">
<title>Selka Marven Photography – Business Card</title>
<link rel="stylesheet" href="https://fonts.googleapis.com/css2?family=Open+Sans:wght@400&display=swap">
<style>
  :root {
    --stage: #d6d6d6;
    --card-light: #ffffff;
    --card-dark: #5c5c5c;
    --ink: #5c5c5c;
    --ink-on-dark: #f2f2f2;
    --rule: #bdbdbd;
  }
  * { margin: 0; padding: 0; box-sizing: border-box; }
  html, body {
    width: 1200px;
    height: 932px;
    overflow: hidden;
    background: var(--stage);
    font-family: "Open Sans", Arial, sans-serif;
  }
  .card-set {
    position: relative;
    width: 1200px;
    height: 932px;
  }
  .card {
    position: absolute;
    top: 116px;
    width: 400px;
    height: 700px;
    border-radius: 26px;
    box-shadow: 0 6px 18px rgba(0,0,0,0.18);
  }
  .card--front { left: 170px; background: var(--card-light); color: var(--ink); }
  .card--back  { left: 630px; background: var(--card-dark); color: var(--ink-on-dark); }

  .brand-name {
    position: absolute;
    left: 0;
    right: 0;
    top: 290px;
    text-align: center;
    font-size: 17px;
    font-weight: 400;
    letter-spacing: 4px;
    text-transform: uppercase;
    line-height: 1.6;
  }
  .card--back .brand-name { top: 300px; }

  .contact {
    position: absolute;
    left: 40px;
    right: 40px;
    bottom: 46px;
    text-align: center;
    font-size: 16px;
    line-height: 1.5;
  }
  .contact__rule {
    height: 1px;
    background: var(--rule);
    margin: 8px 0;
  }
  .contact__divider {
    display: flex;
    align-items: center;
    justify-content: center;
    gap: 6px;
    margin: 4px 0;
  }
  .contact__divider span {
    width: 70px;
    height: 1px;
    background: var(--rule);
  }
  .contact__divider svg { display: block; }
</style>
</head>
<body>
  <main class="card-set">
    <section class="card card--front" aria-label="Card front">
      <p class="brand-name">Selka Marven<br>Photography</p>
      <div class="contact">
        <div class="contact__rule"></div>
        <p class="contact__phone">555-203-1946</p>
        <p class="contact__email">selkamarvenphoto@mailbox-demo.com</p>
        <div class="contact__divider">
          <span></span>
          <svg width="8" height="8" viewBox="0 0 8 8"><circle cx="4" cy="4" r="3.5" fill="#5c5c5c"/></svg>
          <span></span>
        </div>
        <p class="contact__web">www.selkamarvenphotography-demo.com</p>
        <p class="contact__address">Selka Marven Photography, Alder Falls VT</p>
        <div class="contact__rule"></div>
      </div>
    </section>

    <section class="card card--back" aria-label="Card back">
      <p class="brand-name">Selka Marven<br>Photography</p>
    </section>
  </main>
</body>
</html>
```